Design Brief: Tidewell Group Business Card Design
Project Overview

Tidewell Group is a strategic partner to entrepreneurs and leadership teams, supporting business growth through clarity, execution, and trusted expertise. We are looking for a premium, modern business card design that reflects confidence, professionalism, and upward momentum.

Main logo the one with gold bar for the Tidewell Group.

This card will be used by executives and staff across the Tidewell Group business.

Brand Personality
Professional but human
Confident but collaborative
Strategic, credible, and execution-focused
Premium without being flashy

This is not a startup, tech gimmick, or overly creative brand.

Card Format
Portrait orientation (vertical)
Standard size: 55 × 90 mm
Two-sided
One corner cut (top-right corner preferred) to subtly represent upward movement and growth

Design must still work if corner cutting is not available with certain printers

Front Side (Contact Details)
Include:
Tidewell Group logo (provided)
Name
Title
Phone number
Email address
Website
Optional: tagline at the bottom

Style:
Clean
Minimal
Plenty of white space
Easy to read

Back Side (Ecosystem / Brand Message)
Include:
Heading such as: “The Tidewell Network”
Short 2–3 line description explaining that Tidewell is a strategic partner with an ecosystem of specialist professional services businesses operating across Strategic Advisory, Capital Raising, People, & Finance.

This side should reinforce scale, capability, and partnership, not sales messaging.

Colours
Primary brand colours:
Tidewell Blue: #0063B0
Deep Blue: #1A3D6D
Gold accent (very subtle use only): #C9A24D

Rules:
No gradients
No bright or neon colours
No heavy textures
Gold should be minimal and refined

Typography
Clean, modern sans-serif
Professional and readable
No script or decorative fonts

What to Avoid
Landscape layouts (Unless recommended based on logo design, which is horizontal in nature)
Overdesigned or cluttered cards
Loud colours or gradients
Trendy effects that won’t age well

Multiple accent colours

Deliverables
Print-ready files (PDF)
Editable source files (AI / PSD)
Front and back designs

Mockups showing the portrait card and cut corner

Target Outcome
A business card that feels:
Executive
Distinctive
Timeless
Aligned to a strategic, multi-division business

Target Market(s)

Business Owners and Executives (Across industries)

Industry/Entity Type

Professional Services

Contact Information for Business Card

First name and Surname, Email address, Cell phone number, website

Font styles to use
Other font styles liked:
• IBM Plex Sans and or Sans Pro

Colors
0054AA
0677BA
7BADD7
CADEEF
E8F1F8

Requirements
Must have
• Include QR code to digital business card.

```html
<!DOCTYPE html>
<html lang="en">
<head>
<meta charset="utf-8">
<title>Tidewell Group — Business Card</title>
<link rel="stylesheet" href="https://fonts.googleapis.com/css2?family=Montserrat:ital,wght@0,500;0,600;0,800;0,900;1,600&display=swap">
<style>
  :root {
    --tidewell-blue: #0673BA;
    --ink: #111111;
    --gold: #C9A24D;
    --paper: #FAFAFA;
    --backdrop: #F3F3F3;
    --white: #FFFFFF;
  }
  * { box-sizing: border-box; margin: 0; padding: 0; }
  html, body { width: 1200px; height: 1200px; overflow: hidden; }
  body {
    background: var(--backdrop);
    font-family: "Montserrat", Arial, sans-serif;
    position: relative;
  }
  .card {
    position: absolute;
    top: 276px;
    width: 390px;
    height: 638px;
    overflow: hidden;
  }
  .card--front { left: 200px; background: var(--paper); }
  .card--back { left: 610px; background: var(--tidewell-blue); color: var(--white); }

  .gold-rule {
    position: absolute;
    top: 0; bottom: 0;
    width: 2px;
    background: var(--gold);
  }
  .card--front .gold-rule { left: 369px; }
  .card--back .gold-rule { left: 22px; }

  .brand {
    position: absolute;
    left: 36px;
    top: 44px;
  }
  .brand__name {
    font-weight: 900;
    font-size: 27px;
    line-height: 0.98;
    color: var(--ink);
    text-transform: uppercase;
    letter-spacing: 0.2px;
  }
  .brand__tagline {
    margin-top: 8px;
    font-style: italic;
    font-weight: 600;
    font-size: 9px;
    line-height: 1.15;
    color: var(--ink);
  }

  .person {
    position: absolute;
    left: 36px;
    top: 250px;
    color: var(--tidewell-blue);
  }
  .person__name {
    font-weight: 800;
    font-size: 42px;
    line-height: 1.06;
    text-transform: uppercase;
  }
  .person__title {
    font-weight: 500;
    font-size: 27px;
    line-height: 1.1;
  }

  .contact {
    position: absolute;
    left: 39px;
    top: 530px;
    list-style: none;
    color: var(--tidewell-blue);
    font-weight: 600;
    font-size: 13.5px;
  }
  .contact__item {
    display: flex;
    align-items: center;
    gap: 10px;
    height: 24px;
    margin-bottom: 2px;
  }
  .contact__item:last-child { margin-top: 4px; }
  .contact__icon { width: 21px; height: 21px; flex: none; }

  .network {
    position: absolute;
    left: 42px;
    right: 30px;
    top: 466px;
  }
  .network__title {
    font-weight: 800;
    font-size: 49px;
    line-height: 0.78;
    text-transform: uppercase;
    letter-spacing: -0.5px;
  }
  .network__text {
    margin-top: 10px;
    font-weight: 500;
    font-size: 10px;
    line-height: 0.98;
  }
</style>
</head>
<body>

<section class="card card--front" aria-label="Business card, front">
  <div class="brand">
    <div class="brand__name">Tidewell<br>Group</div>
    <p class="brand__tagline">Building Clarity. Sustaining Momentum.<br>Delivering Results.</p>
  </div>

  <div class="person">
    <h1 class="person__name">Name<br>Surename</h1>
    <p class="person__title">Your Title</p>
  </div>

  <ul class="contact">
    <li class="contact__item">
      <svg class="contact__icon" viewBox="0 0 24 24" fill="none" stroke="currentColor" stroke-width="1.6" stroke-linecap="round" stroke-linejoin="round" aria-hidden="true">
        <path d="M5 3.5l3 .2 1.5 4-2 1.6a11 11 0 0 0 6.2 6.2l1.6-2 4 1.5.2 3a2 2 0 0 1-2.2 2A17 17 0 0 1 3 5.7a2 2 0 0 1 2-2.2z"/>
        <path d="M14 3.5a6.5 6.5 0 0 1 6.5 6.5M14 6.8a3.2 3.2 0 0 1 3.2 3.2"/>
      </svg>
      <span>0123 4567 8910</span>
    </li>
    <li class="contact__item">
      <svg class="contact__icon" viewBox="0 0 24 24" fill="none" stroke="currentColor" stroke-width="1.6" stroke-linejoin="round" aria-hidden="true">
        <rect x="2.5" y="5" width="19" height="14"/>
        <path d="M2.5 5l9.5 8 9.5-8M2.5 19l7-6.5M21.5 19l-7-6.5"/>
      </svg>
      <span>name@tidewellgroup.com</span>
    </li>
    <li class="contact__item">
      <svg class="contact__icon" viewBox="0 0 24 24" fill="none" stroke="currentColor" stroke-width="1.5" aria-hidden="true">
        <circle cx="12" cy="12" r="9.5"/>
        <ellipse cx="12" cy="12" rx="4.2" ry="9.5"/>
        <path d="M2.5 12h19M4 7h16M4 17h16M12 2.5v19"/>
      </svg>
      <span>www.tidewellgroup.com</span>
    </li>
  </ul>

  <div class="gold-rule"></div>
</section>

<section class="card card--back" aria-label="Business card, back">
  <div class="gold-rule"></div>
  <div class="network">
    <h2 class="network__title">The<br>Tidewell<br>Network</h2>
    <p class="network__text">Tidewell brings together a group of specialist firms giving growing businesses expert support in strategy, funding, talent and financial management.</p>
  </div>
</section>

</body>
</html>
```